bramblewood ridge livestock company website

we would like a home page, an about us page, a page for sires, a page for dams, A sale page where we can list progreny for sale and a contact us. on the about us page we would like there to be a family picture. on the sires page we would like to have a picture of each sire, a description beside them and a link to their online profile at prairie hereford. on the dam page we would like to have a picture of each dam, aswell as a description beside them aswell as a link to the prairie hereford site. would like the website to very mobile phone friendly as expecting most traffic to be on phone. we would like the website to look and feel very mich like a farm, rustic, barbed wire and other farm feels. we would also like a frozen genetics pages where we can include pictures and descriptions of the sires and dams aswell as a price for embryos and semen. we need to website to be easy to maintain so we can update pictures and information as it changes, we would like there to be a feature so that people can sign up to be on our mailing list by giving us their mailing addess and email and full name
aswell as an area where they can send us a message to contact us.

leaving for work for 3 weeks in the canadian arctic will have limited ability to use the internet

Target Market(s)

other ranchers, farmers, cattlemen,

Industry/Entity Type

farming, agriculture, cattle

Coding

Coded - Design and coding required

Requirements
Must have
• about page, contact page, sires page, dams page, SALE page.
Nice to have
• country/farm vibe, barbed wire, wood,

```html
<!DOCTYPE html>
<html lang="en">
<head>
<meta charset="utf-8">
<title>Bramblewood Ridge Livestock Company</title>
<link href="https://fonts.googleapis.com/css2?family=Poppins:wght@400;500;600&display=swap" rel="stylesheet">
<style>
:root{
  --brown:#7b3508;
  --brown-dark:#5e2806;
  --ink:#1d1d1d;
  --navy:#1c2d4f;
  --muted:#5a5a5a;
  --cream:#fdf0d2;
  --gold:#f2b035;
  --white:#ffffff;
}
*{box-sizing:border-box;margin:0;padding:0}
html,body{width:1200px;height:3062px;overflow:hidden}
body{position:relative;background:var(--white);font-family:'Poppins',sans-serif;color:var(--ink)}
.abs{position:absolute}
a{color:inherit;text-decoration:none}

/* header */
.brand{left:50px;top:22px;width:90px;text-align:center;font-weight:600;font-size:11px;line-height:13px;color:var(--ink);letter-spacing:.3px}
.brand .mark{display:block;width:26px;height:26px;margin:0 auto 3px;border-radius:50%;background:var(--ink)}
.nav{top:34px;left:0;width:100%;font-size:15px;color:#2a2a2a}
.nav a{position:absolute;white-space:nowrap}
.nav a.active{color:var(--brown);font-weight:500;border-bottom:2px solid var(--brown);padding-bottom:1px}
.btn-start{left:1012px;top:27px;width:138px;height:38px;border-radius:10px;background:var(--brown);color:var(--white);font-size:14px;display:flex;align-items:center;justify-content:center}

/* hero */
.hero{left:17px;top:83px;width:1166px;height:815px;border-radius:20px;overflow:hidden;
  background:linear-gradient(180deg,#2c2a27 0%,#4a4640 30%,#5d5a52 50%,#6b5b45 75%,#4b3e2f 100%)}
.hero-shade{left:0;top:0;width:100%;height:100%;background:rgba(0,0,0,.28)}
.hero-title{left:0;top:250px;width:100%;text-align:center;color:var(--white);font-weight:600;font-size:51px;line-height:75px}
.hero-sub{left:0;top:419px;width:100%;text-align:center;color:#f1e6cf;font-size:26px;line-height:40px;font-weight:400}
.btn{display:flex;align-items:center;justify-content:center;gap:8px;font-size:14px;font-weight:500;border-radius:10px;height:48px}
.btn-solid{background:var(--brown);color:var(--white)}
.btn-ghost{border:2px solid var(--white);color:var(--white)}

/* features */
.feature{width:360px;text-align:center}
.feature .icon{width:60px;height:60px;border-radius:50%;background:var(--cream);margin:0 auto;display:flex;align-items:center;justify-content:center}
.feature h3{color:var(--brown);font-weight:600;font-size:18px;margin-top:35px}
.feature p{color:var(--muted);font-size:14px;line-height:22px;margin:20px auto 0;width:300px}

/* featured */
.band{left:0;top:1265px;width:1200px;height:642px;background:var(--brown)}
.band-title{left:0;top:1296px;width:100%;text-align:center;color:var(--white);font-size:36px;font-weight:600;line-height:52px}
.card{width:530px;height:446px;top:1392px;background:var(--white);border-radius:20px}
.card .photo{position:absolute;left:24px;top:21px;width:483px;height:250px;border-radius:12px}
.card h3{position:absolute;left:24px;top:288px;color:var(--navy);font-size:20px;font-weight:600}
.card p{position:absolute;left:24px;top:325px;width:370px;color:var(--navy);font-size:14px;line-height:23px}
.card .pill{position:absolute;left:24px;top:388px;height:33px;padding:0 18px;border-radius:17px;background:var(--brown);color:var(--white);font-size:14px;font-weight:500;display:flex;align-items:center;gap:8px;box-shadow:0 3px 6px rgba(0,0,0,.2)}

/* testimonials */
.reviews-title{left:0;top:1975px;width:100%;text-align:center;font-size:40px;font-weight:600;color:#111}
.review{top:2100px;width:317px;height:212px;background:var(--white);border-radius:12px;box-shadow:0 10px 35px rgba(0,0,0,.13)}
.review .q{position:absolute;left:25px;top:-24px;width:44px;height:44px;border-radius:50%;background:var(--brown);color:var(--white);font-size:26px;font-weight:600;display:flex;align-items:center;justify-content:center}
.review .stars{position:absolute;left:24px;top:38px;color:var(--gold);font-size:13px;letter-spacing:3px}
.review .text{position:absolute;left:24px;top:67px;width:270px;font-size:12px;line-height:20px;color:#555}
.review .rule{position:absolute;left:0;top:152px;width:100%;height:1px;background:#ececec}
.review .avatar{position:absolute;left:24px;top:166px;width:28px;height:28px;border-radius:50%;background:#c9c2b8}
.review .name{position:absolute;left:63px;top:166px;font-size:11px;color:#222;font-weight:500}
.review .role{position:absolute;left:63px;top:182px;font-size:9px;color:#999}

/* call to action */
.cta-arc{left:0;top:2380px;width:1200px;height:400px}
.cta-title{left:0;top:2515px;width:100%;text-align:center;color:var(--white);font-size:37px;font-weight:600}
.cta-text{left:0;top:2580px;width:100%;text-align:center;color:#f1e3d3;font-size:17px;line-height:28px}
.btn-contact{left:507px;top:2675px;width:186px;height:48px;border:1.5px solid var(--white);border-radius:10px;color:var(--white);font-size:14px;font-weight:500;display:flex;align-items:center;justify-content:center;gap:8px}

/* footer */
.footer{left:0;top:2775px;width:1200px;height:287px;background:var(--brown);border-top:1px solid rgba(255,255,255,.35)}
.foot-brand{left:62px;top:2815px;width:100px;text-align:center;font-weight:600;font-size:11px;line-height:13px;color:#1a1a1a}
.foot-brand .mark{display:block;width:26px;height:26px;margin:0 auto 3px;border-radius:50%;background:#1a1a1a}
.foot-about{left:69px;top:2897px;width:360px;color:#f4e5d5;font-size:19px;line-height:28px}
.foot-col h4{color:var(--white);font-size:17px;font-weight:500;margin-bottom:12px}
.foot-col a{display:block;color:#f4e5d5;font-size:14px;line-height:20px;margin-bottom:13px}
.foot-col a.u{text-decoration:underline;color:var(--white)}
.foot-rule{left:60px;top:3005px;width:1080px;height:1px;background:rgba(255,255,255,.5)}
.copy{left:0;top:3028px;width:100%;text-align:center;color:#f4e5d5;font-size:11px}
.social{top:3022px;width:28px;height:28px;border:1.5px solid var(--white);border-radius:5px}
.social i{position:absolute;left:8px;top:8px;width:9px;height:9px;border:1.5px solid var(--white);border-radius:2px}
</style>
</head>
<body>

<header>
  <div class="abs brand"><span class="mark"></span>BRAMBLEWOOD RIDGE</div>
  <nav class="abs nav">
    <a class="active" style="left:317px">Home</a>
    <a style="left:408px">About Us</a>
    <a style="left:525px">Sires</a>
    <a style="left:610px">Dams</a>
    <a style="left:703px">Sale</a>
    <a style="left:780px">Frozen Genetics</a>
  </nav>
  <a class="abs btn-start">Get Started</a>
</header>

<section class="abs hero">
  <div class="abs hero-shade" role="img" aria-label="Photo of cattle feeding along a rail inside a barn"></div>
  <h1 class="abs hero-title">Welcome to Bramblewood Ridge<br>Livestock Company</h1>
  <p class="abs hero-sub">Raising premium Angus cattle with a commitment to quality genetics<br>and excellence in breeding</p>
  <a class="abs btn btn-solid" style="left:415px;top:532px;width:175px">Visit Our Sires
    <svg width="20" height="12" viewBox="0 0 20 12"><path d="M1 6h17M13 1l5 5-5 5" fill="none" stroke="#fff" stroke-width="1.6"/></svg></a>
  <a class="abs btn btn-ghost" style="left:608px;top:532px;width:143px">Browse Sales</a>
</section>

<section>
  <div class="abs feature" style="left:17px;top:967px">
    <div class="icon"><svg width="30" height="20" viewBox="0 0 30 20"><rect x="4" y="5" width="20" height="8" rx="2" fill="#a0522d"/><rect x="6" y="13" width="2" height="6" fill="#a0522d"/><rect x="20" y="13" width="2" height="6" fill="#a0522d"/></svg></div>
    <h3>Premium Genetics</h3>
    <p>Our carefully selected sires and dams produce exceptional offspring with superior genetics</p>
  </div>
  <div class="abs feature" style="left:420px;top:967px">
    <div class="icon"><svg width="24" height="24" viewBox="0 0 24 24"><path d="M6 20L18 6" stroke="#c89a3a" stroke-width="2"/><circle cx="15" cy="9" r="2" fill="#c89a3a"/><circle cx="12" cy="12" r="2" fill="#c89a3a"/></svg></div>
    <h3>Sustainable Farming</h3>
    <p>Committed to sustainable and ethical farming practices for healthy, quality cattle</p>
  </div>
  <div class="abs feature" style="left:823px;top:967px">
    <div class="icon"><svg width="24" height="24" viewBox="0 0 24 24"><path d="M7 4h10v5a5 5 0 0 1-10 0z" fill="#e0a020"/><rect x="11" y="14" width="2" height="4" fill="#e0a020"/><rect x="8" y="18" width="8" height="2" fill="#b07010"/></svg></div>
    <h3 style="margin-top:42px">Proven Excellence</h3>
    <p style="margin-top:30px">Registered Prairie Hereford cattle with documented lineage and performance records</p>
  </div>
</section>

<section>
  <div class="abs band"></div>
  <h2 class="abs band-title">Featured Livestock</h2>
  <div class="abs card" style="left:43px">
    <div class="photo" role="img" aria-label="Photo of a sire standing in an autumn pasture" style="background:linear-gradient(180deg,#7c6a3e,#9a8450 55%,#6d5a33)"></div>
    <h3>Our Sires</h3>
    <p>Explore our outstanding collection of registered Angus sires with proven genetics</p>
    <a class="pill">View Sires <svg width="18" height="12" viewBox="0 0 20 12"><path d="M1 6h17M13 1l5 5-5 5" fill="none" stroke="#fff" stroke-width="1.6"/></svg></a>
  </div>
  <div class="abs card" style="left:627px">
    <div class="photo" role="img" aria-label="Photo of an animal drinking from a farmyard pond" style="background:linear-gradient(180deg,#7e8a8c,#8a7a62 40%,#3d6da8 70%,#2f5d97)"></div>
    <h3>Our Dams</h3>
    <p>Meet our exceptional breeding females known for maternal excellence and quality offspring</p>
    <a class="pill">View Dams <svg width="18" height="12" viewBox="0 0 20 12"><path d="M1 6h17M13 1l5 5-5 5" fill="none" stroke="#fff" stroke-width="1.6"/></svg></a>
  </div>
</section>

<section>
  <h2 class="abs reviews-title">What Our Clients Are Saying</h2>
  <div class="abs review" style="left:97px">
    <div class="q">&#8220;</div><div class="stars">★★★★★</div>
    <p class="text">Great experience working with the team. They perfectly captured the vision of Bramblewood Ridge and delivered a professional result.</p>
    <div class="rule"></div><div class="avatar"></div>
    <div class="name">Mara Lindqvist</div><div class="role">Rancher, Alberta</div>
  </div>
  <div class="abs review" style="left:442px">
    <div class="q">&#8220;</div><div class="stars">★★★★★</div>
    <p class="text">Great experience working with the team. They perfectly captured the vision of Bramblewood Ridge and delivered a professional result.</p>
    <div class="rule"></div><div class="avatar"></div>
    <div class="name">Owen Halvorsen</div><div class="role">Owner, Tall Pine Farm</div>
  </div>
  <div class="abs review" style="left:785px">
    <div class="q">&#8220;</div><div class="stars">★★★★★</div>
    <p class="text">Great experience working with the team. They perfectly captured the vision of Bramblewood Ridge and delivered a professional result.</p>
    <div class="rule"></div><div class="avatar"></div>
    <div class="name">Tessa Kowalchuk</div><div class="role">Rancher, Alberta</div>
  </div>
</section>

<section>
  <svg class="abs cta-arc" viewBox="0 0 1200 400" preserveAspectRatio="none">
    <path d="M0 290 Q600 -190 1200 290 L1200 400 L0 400 Z" fill="#7b3508"/>
  </svg>
  <h2 class="abs cta-title">Ready To Improve Your Herd?</h2>
  <p class="abs cta-text">Browse our current sale listings or contact us to discuss your<br>breeding goals</p>
  <a class="abs btn-contact">Contact Us <svg width="18" height="12" viewBox="0 0 20 12"><path d="M1 6h17M13 1l5 5-5 5" fill="none" stroke="#fff" stroke-width="1.6"/></svg></a>
</section>

<footer>
  <div class="abs footer"></div>
  <div class="abs foot-brand"><span class="mark"></span>BRAMBLEWOOD RIDGE</div>
  <p class="abs foot-about">Raising premium Angus cattle with a commitment to quality genetics and excellence in breeding</p>
  <div class="abs foot-col" style="left:677px;top:2813px">
    <h4>Quick Links</h4>
    <a class="u">Home</a><a>About Us</a><a>Sires</a><a>Dams</a>
  </div>
  <div class="abs foot-col" style="left:887px;top:2813px">
    <h4>Contact Us</h4>
    <a class="u">hello@bramblewoodridge.ca</a><a class="u">+1 555 014 2000</a><a>Lorem ipsum</a>
  </div>
  <div class="abs foot-rule"></div>
  <p class="abs copy">© 2026 Bramblewood Ridge. All rights reserved.</p>
  <a class="abs social" style="left:1000px" aria-label="Professional network"><i></i></a>
  <a class="abs social" style="left:1042px" aria-label="Social page"><i></i></a>
  <a class="abs social" style="left:1084px" aria-label="Photo feed"><i></i></a>
</footer>

</body>
</html>
```